Endocrinologist needs new stationery

I have a logo from MarkForge and now need stationery with the new logo.

Address: Suite 4, 282 Falcon Street, Richmond, VIC 3121
Phone: 03 9417 2253
Fax: 03 9417 2255
Website: www.drmaylacorwen.com.au
Email: admin@drmaylacorwen.com.au

```html
<!DOCTYPE html>
<html lang="en">
<head>
<meta charset="utf-8">
<title>Dr Mayla Corwen – Letterhead</title>
<link rel="stylesheet" href="https://fonts.googleapis.com/css2?family=Lato:wght@400;700&family=Arimo:wght@400&display=swap">
<style>
  :root {
    --brand-blue: #2f6b9c;
    --brand-plum: #6d4c66;
    --paper: #ffffff;
    --ink: #111111;
    --backdrop: #d9d9d9;
    --header-text: #ffffff;
  }
  * { box-sizing: border-box; margin: 0; padding: 0; }
  html, body { width: 1200px; height: 1159px; overflow: hidden; }
  body {
    background: var(--backdrop);
    display: flex;
    align-items: center;
    justify-content: center;
  }
  .letterhead {
    position: relative;
    width: 780px;
    height: 1103px;
    background: var(--paper);
    box-shadow: 0 6px 24px rgba(0,0,0,0.18);
    overflow: hidden;
  }
  .masthead {
    position: absolute;
    top: 0; left: 0; right: 0;
    height: 126px;
    background: var(--brand-blue);
    display: flex;
    align-items: center;
    padding: 0 40px 0 44px;
    color: var(--header-text);
    font-family: "Lato", sans-serif;
  }
  .masthead-rule {
    position: absolute;
    top: 126px; left: 0; right: 0;
    height: 5px;
    background: var(--brand-plum);
  }
  .brand {
    display: flex;
    flex-direction: column;
    width: 290px;
  }
  .brand-name {
    font-family: "Lato", sans-serif;
    font-weight: 400;
    font-size: 36px;
    letter-spacing: 0.5px;
    line-height: 1.05;
  }
  .brand-specialty {
    font-family: "Lato", sans-serif;
    font-weight: 400;
    font-size: 12px;
    letter-spacing: 1.5px;
    margin-top: 6px;
    padding-top: 5px;
    border-top: 1px solid rgba(255,255,255,0.7);
    width: 190px;
  }
  .masthead-divider {
    width: 1px;
    height: 66px;
    background: rgba(255,255,255,0.7);
    margin: 0 22px 0 8px;
  }
  .contact {
    display: grid;
    grid-template-columns: auto auto;
    column-gap: 22px;
    row-gap: 7px;
    font-size: 13px;
    letter-spacing: 0.3px;
  }
  .contact-item {
    display: flex;
    align-items: center;
    gap: 8px;
    white-space: nowrap;
  }
  .contact-item.address { grid-column: 1 / span 2; }
  .contact-icon {
    width: 18px; height: 18px;
    background: var(--brand-plum);
    border-radius: 3px;
    display: flex;
    align-items: center;
    justify-content: center;
    flex: none;
  }
  .contact-icon svg { width: 12px; height: 12px; fill: #ffffff; }

  .letter-body {
    position: absolute;
    top: 210px;
    left: 150px;
    right: 110px;
    font-family: "Arimo", Arial, sans-serif;
    font-size: 14.5px;
    line-height: 1.12;
    color: var(--ink);
  }
  .letter-body p { margin-bottom: 38px; }

  .signature {
    position: absolute;
    left: 180px;
    top: 925px;
    width: 250px;
    height: 78px;
    background: linear-gradient(90deg, #e9e9e9, #f4f4f4);
    border-radius: 4px;
  }

  .footer-band {
    position: absolute;
    bottom: 0;
    height: 20px;
  }
  .footer-band.primary { left: 0; width: 560px; background: var(--brand-blue); }
  .footer-band.accent { left: 572px; right: 0; height: 26px; background: var(--brand-plum); }
</style>
</head>
<body>
  <main class="letterhead">
    <header class="masthead">
      <div class="brand">
        <span class="brand-name">Dr Mayla Corwen</span>
        <span class="brand-specialty">ENDOCRINOLOGY</span>
      </div>
      <div class="masthead-divider"></div>
      <div class="contact">
        <div class="contact-item phone">
          <span class="contact-icon"><svg viewBox="0 0 24 24"><path d="M6.6 10.8a15 15 0 0 0 6.6 6.6l2.2-2.2a1 1 0 0 1 1-.25 11.4 11.4 0 0 0 3.6.57 1 1 0 0 1 1 1V20a1 1 0 0 1-1 1A17 17 0 0 1 3 4a1 1 0 0 1 1-1h3.5a1 1 0 0 1 1 1c0 1.25.2 2.45.57 3.6a1 1 0 0 1-.25 1z"/></svg></span>
          03 9417 2253
        </div>
        <div class="contact-item email">
          <span class="contact-icon"><svg viewBox="0 0 24 24"><path d="M3 5h18v14H3z M3 5l9 7 9-7" fill="none" stroke="#fff" stroke-width="2"/></svg></span>
          admin@drmaylacorwen.com.au
        </div>
        <div class="contact-item fax">
          <span class="contact-icon"><svg viewBox="0 0 24 24"><path d="M6 3h9l3 3v4H6z M3 10h18v10H3z M7 13h2v2H7z M11 13h2v2h-2z M15 13h2v2h-2z"/></svg></span>
          03 9417 2255
        </div>
        <div class="contact-item web">
          <span class="contact-icon"><svg viewBox="0 0 24 24"><circle cx="12" cy="12" r="9" fill="none" stroke="#fff" stroke-width="2"/><path d="M3 12h18 M12 3c3 3 3 15 0 18 M12 3c-3 3-3 15 0 18" fill="none" stroke="#fff" stroke-width="1.5"/></svg></span>
          www.drmaylacorwen.com.au
        </div>
        <div class="contact-item address">
          <span class="contact-icon"><svg viewBox="0 0 24 24"><path d="M12 2a7 7 0 0 0-7 7c0 5 7 13 7 13s7-8 7-13a7 7 0 0 0-7-7zm0 9.5A2.5 2.5 0 1 1 12 6.5a2.5 2.5 0 0 1 0 5z"/></svg></span>
          Suite 4, 282 Falcon Street, Richmond, VIC 3121
        </div>
      </div>
    </header>
    <div class="masthead-rule"></div>

    <section class="letter-body">
      <p>Lorem ipsum dolor sit amet, consectetur adipiscing elit. Donec fringilla neque euismod volutpat cursus. Vestibulum ac pretium orci, consequat elementum velit. Etiambibendumpurusacauguefinibusvolutpat.Vestibulumjustonisl</p>
      <p>Lorem ipsum dolor sit amet, consectetur adipiscing elit. Donec fringilla neque euismod volutpat cursus. Vestibulum ac pretium orci, consequat elementum velit. Etiambibendumpurusacauguefinibusvolutpat.Vestibulumjustonisl</p>
      <p>Lorem ipsum dolor sit amet, consectetur adipiscing elit. Donec fringilla neque euismod volutpat cursus. Vestibulum ac pretium orci, consequat elementum velit. Etiam bibendum purus ac augue finibus volutpat. Vestibulum justo nisl, gravida aliquet sollicitudin ut, finibus vitae mi. Praesent aliquet scelerisque blandit. Sed id varius lacus, id tristique sem. Fusce et lobortis leo. Aliquam mollis pellentesque magna,condimentumullamcorperexullamcorpernon.Morbiultriciesnunceutellus dignissim,egetvenenatisdolorullamcorper.Etiamdoloreros,iaculisatultriciesnec, volutpatnecorci.Vivamustinciduntrutrumsapien,acporttitormauristristiquenec.</p>
      <p>Lorem ipsum dolor sit amet, consectetur adipiscing elit. Donec fringilla neque euismod volutpat cursus. Vestibulum ac pretium orci, consequat elementum velit. Etiam bibendum purus ac augue finibus volutpat. Vestibulum justo nisl, gravida aliquet sollicitudin ut, finibus vitae mi. Praesent aliquet scelerisque blandit. Sed id varius lacus, id tristique sem. Fusce et lobortis leo. Aliquam mollis pellentesque magna,condimentumullamcorperexullamcorpernon.Morbiultriciesnunceutellus dignissim,egetvenenatisdolorullamcorper.Etiamdoloreros,iaculisatultriciesnec, volutpatnecorci.Vivamustinciduntrutrumsapien,acporttitormauristristiquenec.</p>
      <p>Lorem ipsum dolor sit amet, consectetur adipiscing elit. Donec fringilla neque euismod volutpat cursus. Vestibulum ac pretium orci, consequat elementum velit. Etiambibendumpurusacauguefinibusvolutpat.Vestibulumjustonisl</p>
    </section>

    <div class="signature" role="img" aria-label="Handwritten signature of the sender"></div>

    <div class="footer-band primary"></div>
    <div class="footer-band accent"></div>
  </main>
</body>
</html>
```